Manuka honey wholesales and exports

We need business cards for our honey distribution company based in Tidewell Isles. We supply shops locally and export Manuka honey around the world.
We deal with a very high quality and 100% natural product that can be used for medical, general health as well as food. We are looking business cards that show our honey products are of a high quality with a modern look.

Target Market(s)

Health and medical retailers and importers

Industry/Entity Type

Wholesale

Contact Information for Business Card

Kestrel Hive NZ Limited

www.kestrelhivenz.com

Gareth Moffat

M +64 213958264

E kestrelhivenz@mailbox-example.com

PO Box 47-518
Kowhai Bay
North Shore
Auckland
Tidewell Isles

Font styles to use
Serif

Requirements
Must have
• (Kestrel Hive NZ Limited) with some artwork on one side and all details on the other side.
Nice to have
• I have seen a very simple card with large yellow and black stripes on one side with a company name.. looked clean and simple so something similar or just let the creative beast inside you take over and we will see what you can come up with.

```html
<!DOCTYPE html>
<html lang="en">
<head>
<meta charset="utf-8">
<title>Kestrel Hive NZ Limited – Business Card</title>
<link href="https://fonts.googleapis.com/css2?family=Tinos:wght@400;700&display=swap" rel="stylesheet">
<style>
  :root {
    --backdrop: #3a3330;
    --card-white: #ffffff;
    --card-black: #050505;
    --honey: #f2b705;
    --ink: #111111;
    --paper-text: #f2f2f2;
  }
  * { box-sizing: border-box; margin: 0; padding: 0; }
  html, body {
    width: 1200px; height: 780px; overflow: hidden;
    background: var(--backdrop);
    font-family: "Tinos", "Times New Roman", serif;
  }
  .canvas { position: relative; width: 1200px; height: 780px; }
  .card {
    position: absolute; width: 540px; height: 309px;
    box-shadow: 0 12px 30px rgba(0,0,0,.45);
  }
  /* Front */
  .card-front { left: 40px; top: 120px; background: var(--card-white); }
  .brand-lockup {
    position: absolute; left: 50%; top: 50%;
    transform: translate(-50%, -50%);
    display: flex; align-items: center; gap: 14px;
  }
  .brand-dot { width: 38px; height: 38px; border-radius: 50%; background: var(--honey); flex: none; }
  .brand-name {
    color: var(--ink); font-weight: 700; line-height: 1.05;
    font-size: 30px; letter-spacing: .5px; text-align: right;
    white-space: nowrap;
  }
  .brand-name .brand-sub { display: block; font-size: 18px; }
  /* Back */
  .card-back { left: 620px; top: 350px; background: var(--card-black); }
  .back-title {
    position: absolute; left: 30px; top: 26px;
    color: var(--honey); font-weight: 700; line-height: 1;
    font-size: 28px; letter-spacing: .5px; text-align: right;
    white-space: nowrap;
  }
  .back-title .brand-sub { display: block; font-size: 18px; margin-top: 2px; }
  .contact-block { position: absolute; left: 268px; top: 150px; color: var(--paper-text); white-space: nowrap; }
  .person-name { color: var(--honey); font-weight: 700; font-size: 21px; margin-bottom: 12px; letter-spacing: .3px; }
  .address { font-size: 14px; line-height: 1.2; margin-bottom: 6px; }
  .contact-list { list-style: none; font-size: 14px; }
  .contact-list li { display: flex; align-items: center; gap: 7px; height: 20px; }
  .contact-icon { width: 15px; height: 15px; flex: none; }
</style>
</head>
<body>
<main class="canvas">
  <section class="card card-front" aria-label="Card front">
    <div class="brand-lockup">
      <span class="brand-dot"></span>
      <p class="brand-name">KESTREL HIVE<span class="brand-sub">NZ Limited</span></p>
    </div>
  </section>

  <section class="card card-back" aria-label="Card back">
    <p class="back-title">KESTREL HIVE<span class="brand-sub">NZ Limited</span></p>
    <div class="contact-block">
      <p class="person-name">Gareth Moffat</p>
      <p class="address">PO Box 47-518, Kowhai Bay<br>Eastern Shore Harbourton<br>Tidewell Isles</p>
      <ul class="contact-list">
        <li>
          <svg class="contact-icon" viewBox="0 0 16 16" aria-hidden="true">
            <rect width="16" height="16" fill="var(--honey)"/>
            <rect x="5" y="2.5" width="6" height="11" rx="1" fill="none" stroke="#000" stroke-width="1.2"/>
            <line x1="7" y1="11.5" x2="9" y2="11.5" stroke="#000" stroke-width="1"/>
          </svg>
          +64 213958264
        </li>
        <li>
          <svg class="contact-icon" viewBox="0 0 16 16" aria-hidden="true">
            <rect width="16" height="16" fill="var(--honey)"/>
            <rect x="2.5" y="4.5" width="11" height="7" fill="none" stroke="#000" stroke-width="1.2"/>
            <polyline points="2.5,4.5 8,9 13.5,4.5" fill="none" stroke="#000" stroke-width="1.2"/>
          </svg>
          kestrelhivenz@mailbox-example.com
        </li>
        <li>
          <svg class="contact-icon" viewBox="0 0 16 16" aria-hidden="true">
            <rect width="16" height="16" fill="var(--honey)"/>
            <circle cx="8" cy="8" r="5" fill="none" stroke="#000" stroke-width="1.1"/>
            <ellipse cx="8" cy="8" rx="2.2" ry="5" fill="none" stroke="#000" stroke-width="1"/>
            <line x1="3" y1="8" x2="13" y2="8" stroke="#000" stroke-width="1"/>
          </svg>
          www.kestrelhivenz.com
        </li>
      </ul>
    </div>
  </section>
</main>
</body>
</html>
```